Valve bag design

I need a valve bag for 25kg wall putty bag

Here are attached bags for reference

Most of the words or design you can copy from talvuno bag attached and company profile
Also I have attached our local product for reference

```html
<!DOCTYPE html>
<html lang="en">
<head>
<meta charset="UTF-8">
<title>Nova Glaze Wall Putty – 25kg Valve Bag</title>
<link href="https://fonts.googleapis.com/css2?family=Anton&family=Roboto+Condensed:wght@700&family=Pathway+Gothic+One&family=Archivo:wght@700&display=swap" rel="stylesheet">
<style>
  :root{
    --navy:#243c6b;
    --stripe:#aea49c;
    --white:#ffffff;
    --ink:#1d1d1d;
    --green:#7ed321;
    --backdrop:#a7a8aa;
  }
  *{box-sizing:border-box;margin:0;padding:0}
  html,body{width:1200px;height:1200px;overflow:hidden;background:var(--backdrop)}
  .canvas{position:relative;width:1200px;height:1200px}

  .panel{position:absolute;top:50px;height:1100px;background:var(--white);overflow:hidden}
  .band-top{position:absolute;left:0;top:0;width:100%;height:132px;background:var(--navy)}
  .stripe-top{position:absolute;left:0;top:132px;width:100%;height:15px;background:var(--stripe)}
  .stripe-bottom{position:absolute;left:0;top:980px;width:100%;height:15px;background:var(--stripe)}
  .band-bottom{position:absolute;left:0;top:995px;width:100%;height:105px;background:var(--navy)}

  /* side gusset */
  .bag-gusset{left:220px;width:170px;border-radius:6px 0 0 6px;border-right:2px solid #d9d9d9}
  .gusset-brand{position:absolute;left:0;top:200px;width:100%;text-align:center}
  .gusset-brand .brand-mark{display:block;width:22px;height:22px;margin:0 auto 10px;background:var(--navy)}
  .gusset-brand .brand-name{font-family:"Archivo",sans-serif;font-weight:700;font-size:14px;color:var(--navy);letter-spacing:.5px}
  .gusset-title{position:absolute;left:86px;top:330px;writing-mode:vertical-rl;font-family:"Anton",sans-serif;font-size:66px;line-height:1;color:var(--navy);letter-spacing:1px;text-shadow:2px 2px 0 var(--stripe),-1px -1px 0 var(--stripe),1px -1px 0 var(--stripe),-1px 1px 0 var(--stripe)}
  .gusset-type{position:absolute;left:46px;top:340px;writing-mode:vertical-rl;font-family:"Roboto Condensed",sans-serif;font-weight:700;font-size:24px;line-height:1;color:var(--ink)}
  .gusset-weight{position:absolute;left:40px;top:830px;width:86px;height:86px;border-radius:50%;background:var(--green);color:var(--white);font-family:"Roboto Condensed",sans-serif;font-weight:700;text-align:center;display:flex;flex-direction:column;justify-content:center;line-height:1}
  .gusset-weight .label{font-size:14px}
  .gusset-weight .value{font-size:23px;margin-top:2px}

  /* front face */
  .bag-front{left:390px;width:570px;border-radius:0 6px 6px 0}
  .brand{position:absolute;left:0;top:190px;width:100%;text-align:center}
  .brand .brand-mark{display:block;width:38px;height:38px;margin:0 auto 18px;background:var(--navy)}
  .brand .brand-name{font-family:"Archivo",sans-serif;font-weight:700;font-size:28px;color:var(--navy);letter-spacing:1px}

  .net-weight{position:absolute;left:452px;top:190px;width:100px;height:100px;border-radius:50%;background:var(--green);color:var(--white);font-family:"Roboto Condensed",sans-serif;font-weight:700;text-align:center;display:flex;flex-direction:column;justify-content:center;line-height:1}
  .net-weight .label{font-size:17px}
  .net-weight .value{font-size:27px;margin-top:3px}

  .product-title{position:absolute;left:0;top:312px;width:100%;text-align:center;font-family:"Anton",sans-serif;font-size:84px;line-height:1;color:var(--navy);letter-spacing:-1px;text-shadow:2px 2px 0 var(--stripe),-1px -1px 0 var(--stripe),1px -1px 0 var(--stripe),-1px 1px 0 var(--stripe)}
  .product-type{position:absolute;left:0;top:415px;width:100%;text-align:center;font-family:"Roboto Condensed",sans-serif;font-weight:700;font-size:34px;color:var(--ink)}
  .product-use{position:absolute;left:0;top:488px;width:100%;text-align:center;font-family:"Roboto Condensed",sans-serif;font-weight:700;font-size:22px;line-height:1.5;color:var(--navy)}

  .features{position:absolute;left:100px;top:568px;width:350px;height:492px;background:var(--navy);border:5px solid var(--stripe)}
  .features-title{position:absolute;left:25px;top:24px;font-family:"Pathway Gothic One",sans-serif;font-size:32px;color:var(--white)}
  .feature-list{list-style:none}
  .feature{position:absolute;left:0;width:100%;height:44px;display:flex;align-items:center}
  .feature-icon{position:absolute;left:25px;width:40px;height:44px;border:2px solid var(--white);display:flex;align-items:center;justify-content:center}
  .feature-icon svg{width:26px;height:26px}
  .feature-text{position:absolute;left:80px;font-family:"Pathway Gothic One",sans-serif;font-size:20px;color:var(--white);white-space:nowrap}

  .tick{position:absolute;left:78px;width:44px;height:44px;border-radius:50%;background:var(--green);border:3px solid var(--white);display:flex;align-items:center;justify-content:center}
  .tick svg{width:22px;height:22px}
</style>
</head>
<body>
<div class="canvas">
  <section class="panel bag-gusset">
    <div class="band-top"></div>
    <div class="stripe-top"></div>
    <div class="stripe-bottom"></div>
    <div class="band-bottom"></div>
    <div class="gusset-brand">
      <span class="brand-mark"></span>
      <span class="brand-name">NOVA GLAZE</span>
    </div>
    <div class="gusset-title">WALL PUTTY</div>
    <div class="gusset-type">White Cement Based Putty</div>
    <div class="gusset-weight"><span class="label">Net Wt.</span><span class="value">25kg.</span></div>
  </section>

  <section class="panel bag-front">
    <div class="band-top"></div>
    <div class="stripe-top"></div>
    <div class="stripe-bottom"></div>
    <div class="band-bottom"></div>

    <div class="brand">
      <span class="brand-mark"></span>
      <span class="brand-name">NOVA GLAZE</span>
    </div>

    <div class="net-weight"><span class="label">Net Wt.</span><span class="value">25kg.</span></div>

    <h1 class="product-title">WALL PUTTY</h1>
    <h2 class="product-type">White Cement Based Putty</h2>
    <p class="product-use">Premium wall putty to use for cement based<br>plaster &amp; concrete surfaces before paint</p>

    <div class="features">
      <h3 class="features-title">The Qualities &amp; Features</h3>
      <ul class="feature-list">
        <li class="feature" style="top:86px"><span class="feature-icon"><svg viewBox="0 0 26 26" fill="#fff"><path d="M17 3l1.5 4 4 1.5-4 1.5L17 14l-1.5-4-4-1.5 4-1.5z"/><circle cx="7" cy="18" r="1.5"/><circle cx="12" cy="22" r="1"/></svg></span><span class="feature-text">Very smooth and glossy finish.</span></li>
        <li class="feature" style="top:140px"><span class="feature-icon"><svg viewBox="0 0 26 26" fill="none" stroke="#fff" stroke-width="2"><path d="M5 10l9 9M5 10v7M5 10h7"/><circle cx="20" cy="20" r="3"/></svg></span><span class="feature-text">Suitable for all cement surfaces.</span></li>
        <li class="feature" style="top:194px"><span class="feature-icon"><svg viewBox="0 0 26 26" fill="none" stroke="#fff" stroke-width="2"><path d="M3 13L13 3l10 10M6 11v12h14V11"/><path d="M10 17l2 2 4-4"/></svg></span><span class="feature-text">Suitable for Interior &amp; exterior.</span></li>
        <li class="feature" style="top:248px"><span class="feature-icon"><svg viewBox="0 0 26 26" fill="none" stroke="#fff" stroke-width="2"><path d="M13 1v7M10 5l3 3 3-3M13 25v-7M10 21l3-3 3 3M3 11h20M3 15h20"/></svg></span><span class="feature-text">Very high tensile adhesion.</span></li>
        <li class="feature" style="top:302px"><span class="feature-icon"><svg viewBox="0 0 26 26" fill="#fff"><path d="M6 4c3 5 4 7 4 9a4 4 0 0 1-8 0c0-2 1-4 4-9zM18 4c3 5 4 7 4 9a4 4 0 0 1-8 0c0-2 1-4 4-9z"/><rect x="2" y="20" width="22" height="3"/></svg></span><span class="feature-text">Very low water absorption.</span></li>
        <li class="feature" style="top:356px"><span class="feature-icon"><svg viewBox="0 0 26 26"><path fill="#fff" d="M10 2c5 8 7 11 7 14a7 7 0 0 1-14 0c0-3 2-6 7-14z"/><circle cx="20" cy="20" r="5" fill="#fff"/><path d="M18 18l4 4M22 18l-4 4" stroke="#243c6b" stroke-width="1.6"/></svg></span><span class="feature-text">No water curring needed.</span></li>
        <li class="feature" style="top:410px"><span class="feature-icon"><svg viewBox="0 0 26 26" fill="none" stroke="#fff" stroke-width="2"><rect x="3" y="3" width="20" height="20"/><path d="M8 8l10 10M13 18h5v-5"/></svg></span><span class="feature-text">Very high coverage and easy to apply.</span></li>
      </ul>
    </div>

    <div class="tick" style="top:654px"><svg viewBox="0 0 22 22" fill="none" stroke="#fff" stroke-width="3.5"><path d="M4 11l5 5 9-10"/></svg></div>
    <div class="tick" style="top:708px"><svg viewBox="0 0 22 22" fill="none" stroke="#fff" stroke-width="3.5"><path d="M4 11l5 5 9-10"/></svg></div>
    <div class="tick" style="top:762px"><svg viewBox="0 0 22 22" fill="none" stroke="#fff" stroke-width="3.5"><path d="M4 11l5 5 9-10"/></svg></div>
    <div class="tick" style="top:816px"><svg viewBox="0 0 22 22" fill="none" stroke="#fff" stroke-width="3.5"><path d="M4 11l5 5 9-10"/></svg></div>
    <div class="tick" style="top:870px"><svg viewBox="0 0 22 22" fill="none" stroke="#fff" stroke-width="3.5"><path d="M4 11l5 5 9-10"/></svg></div>
    <div class="tick" style="top:924px"><svg viewBox="0 0 22 22" fill="none" stroke="#fff" stroke-width="3.5"><path d="M4 11l5 5 9-10"/></svg></div>
    <div class="tick" style="top:978px"><svg viewBox="0 0 22 22" fill="none" stroke="#fff" stroke-width="3.5"><path d="M4 11l5 5 9-10"/></svg></div>
  </section>
</div>
</body>
</html>
```